Harbor Rest Company Needs Business Card

Looking for a very nice looking business card. Creative but not extravagant. We sell beds and pillows across the U.S. and need something professional but catchy. I have attached the logo.

Name : Dale Morton
Title : President
Phone : (800) 417-2960
Email: rest@quiltano.com
Website: www.quiltano.com

Can be single-sided or double-sided
horizontal or vertical

Can use Blues/Greys

Target Market(s)

Mass Market

Industry/Entity Type

Retail

Contact Information for Business Card

Name : Dale Morton
Title : President
Phone : (800) 417-2960
Email: rest@quiltano.com
Website: www.quiltano.com

Requirements
Must have
• Clean, Modern, Smooth
• Can use Blues/Greys
• On the other side without the information - have something simple like www.quiltano.com or our logo
Nice to have
• Surprise me
Should not have
• Nothing crazy, nothing cluttered

```html
<!DOCTYPE html>
<html lang="en">
<head>
<meta charset="utf-8">
<title>Quiltano Business Card</title>
<link rel="stylesheet" href="https://fonts.googleapis.com/css2?family=Roboto:wght@300;400;500;700&display=swap">
<style>
  :root {
    --brand-blue: #2ea3dc;
    --text-grey: #555a5e;
    --rule-grey: #d4d6d8;
    --card-white: #ffffff;
    --backdrop: #e9ebed;
  }
  * { margin: 0; padding: 0; box-sizing: border-box; }
  html, body {
    width: 1200px; height: 1000px; overflow: hidden;
    background: var(--backdrop);
    font-family: "Roboto", Arial, sans-serif;
  }
  .card {
    position: absolute;
    left: 243px;
    width: 708px;
    height: 404px;
    background: var(--card-white);
    box-shadow: 0 2px 8px rgba(0,0,0,0.08);
  }
  .card--front { top: 84px; }
  .card--back { top: 526px; }

  .wordmark {
    position: absolute;
    color: var(--brand-blue);
    font-weight: 300;
    line-height: 1;
    letter-spacing: 1px;
  }
  .card--front .wordmark {
    left: 0; right: 0; top: 132px;
    text-align: center;
    font-size: 100px;
  }
  .card--back .wordmark {
    right: 32px; top: 36px;
    font-size: 62px;
  }

  .side-rule {
    position: absolute;
    left: 69px; top: 0; bottom: 0;
    width: 2px;
    background: var(--rule-grey);
  }

  .person {
    position: absolute;
    left: 93px; top: 201px;
  }
  .person__name {
    color: var(--brand-blue);
    font-weight: 700;
    font-size: 18px;
    letter-spacing: 0.3px;
  }
  .person__title {
    color: var(--text-grey);
    font-size: 16px;
    margin-top: 2px;
  }

  .contacts {
    position: absolute;
    left: 59px; top: 264px;
    list-style: none;
  }
  .contacts__item {
    display: flex;
    align-items: center;
    height: 25px;
    color: var(--text-grey);
    font-size: 16px;
  }
  .contacts__icon {
    width: 22px; height: 22px;
    margin-right: 12px;
    flex: none;
  }
</style>
</head>
<body>
  <section class="card card--front">
    <div class="wordmark">quiltano</div>
  </section>

  <section class="card card--back">
    <div class="side-rule"></div>
    <div class="wordmark">quiltano</div>

    <div class="person">
      <div class="person__name">DALE MORTON</div>
      <div class="person__title">President</div>
    </div>

    <ul class="contacts">
      <li class="contacts__item">
        <svg class="contacts__icon" viewBox="0 0 22 22" aria-hidden="true">
          <circle cx="11" cy="11" r="10" fill="var(--brand-blue)"/>
          <path d="M8 6.2l1.6 2.3-1 1.2c.6 1.4 1.7 2.5 3.1 3.1l1.2-1 2.3 1.6-.7 1.8c-3.8-.2-7.2-3.6-7.4-7.4z" fill="#fff"/>
        </svg>
        (800) 417-2960
      </li>
      <li class="contacts__item">
        <svg class="contacts__icon" viewBox="0 0 22 22" aria-hidden="true">
          <circle cx="11" cy="11" r="10" fill="var(--brand-blue)"/>
          <rect x="6" y="7.5" width="10" height="7" fill="#fff"/>
          <path d="M6 7.5l5 4 5-4" fill="none" stroke="var(--brand-blue)" stroke-width="1"/>
        </svg>
        rest@quiltano.com
      </li>
      <li class="contacts__item">
        <svg class="contacts__icon" viewBox="0 0 22 22" aria-hidden="true">
          <circle cx="11" cy="11" r="10" fill="var(--brand-blue)"/>
          <g fill="none" stroke="#fff" stroke-width="1">
            <circle cx="11" cy="11" r="5"/>
            <ellipse cx="11" cy="11" rx="2.2" ry="5"/>
            <path d="M6 11h10M7 8.5h8M7 13.5h8"/>
          </g>
        </svg>
        www.quiltano.com
      </li>
    </ul>
  </section>
</body>
</html>
```